Website for a Construction Business That Builds Houses

We want some design concepts for this website. Customer likes this competitor site: https://copperfernbuilds.com.au/

We have a logo for Varrow Constructions. Logo font is Birdman, attached with AI.

Want to be able to change hero images

Will have a contact page.

Need to know what plugins will be used for WordPress.

```html
<!DOCTYPE html>
<html lang="en">
<head>
<meta charset="utf-8">
<title>Varrow Constructions – Building Your Dream Home</title>
<link rel="stylesheet" href="https://fonts.googleapis.com/css2?family=Righteous&family=Poppins:wght@400;500;600&display=swap">
<style>
:root{
  --green:#7dc242;
  --green-dark:#5d9a2b;
  --ink:#1d1d1d;
  --text:#444;
  --muted:#6b6b6b;
  --panel:#f1f1f1;
  --card-line:#dcdcdc;
  --footer:#262626;
  --footer-text:#d9d9d9;
  --white:#fff;
}
*{box-sizing:border-box;margin:0;padding:0}
html,body{width:1200px;height:4129px;overflow:hidden}
body{position:relative;background:var(--white);font-family:"Poppins",sans-serif;color:var(--ink)}
.abs{position:absolute}
.display{font-family:"Righteous",sans-serif;font-weight:400;text-transform:lowercase;color:var(--ink)}
.rule{display:block;width:64px;height:3px;background:var(--green);margin-top:14px}
.btn{position:absolute;display:flex;align-items:center;justify-content:space-between;background:var(--green);color:var(--ink);border-radius:30px;font-size:13px;font-weight:600;padding:0 4px 0 20px;text-decoration:none;white-space:nowrap}
.btn .arrow{width:30px;height:30px;border-radius:50%;background:var(--white);display:flex;align-items:center;justify-content:center}
.photo{position:absolute;border-radius:10px}

/* hero */
.hero-bg{left:0;top:0;width:1200px;height:570px;background:radial-gradient(ellipse at 20% 40%,#eef6e4 0%,#fff 60%)}
.brand{left:140px;top:18px;display:flex;align-items:center;gap:8px;font-size:20px;font-weight:600;color:var(--ink)}
.brand .dot{width:14px;height:14px;border-radius:50%;background:var(--green)}
.top-contact{top:36px;display:flex;align-items:center;gap:8px;font-size:12.5px;white-space:nowrap}
.hero-photo{left:530px;top:0;width:680px;height:470px;border-radius:0 0 0 330px;background:linear-gradient(160deg,#cfdce8 0%,#9a7a5a 45%,#3d3a36 80%,#6c8f3e 100%)}
.hero-arc{left:510px;top:0;width:700px;height:490px;border-radius:0 0 0 350px;border-left:10px solid #c7e4a8;border-bottom:10px solid #c7e4a8}
.hero-title{left:140px;top:175px;font-size:44px;line-height:57px}
.hero-sub{left:140px;top:370px;font-size:14.5px;line-height:23px;font-weight:500;color:var(--ink)}
.discover{left:30px;top:468px;transform:rotate(-90deg);transform-origin:left top;font-size:9px;letter-spacing:2px;font-weight:600;text-transform:uppercase;white-space:nowrap}
.discover-line{left:36px;top:175px;width:1px;height:175px;background:#bbb}
.mouse{left:29px;top:483px;width:12px;height:18px;border:1.5px solid #333;border-radius:6px}

/* services */
.section-title{width:1200px;text-align:center;font-size:38px}
.section-title .rule{margin:12px auto 0}
.svc{position:absolute;width:283px;height:274px;border-radius:10px}
.svc-card{border:1px solid var(--card-line);background:var(--white);text-align:center;padding:24px 26px}
.svc-card h3{font-size:17px;font-weight:600;margin:18px 0 14px}
.svc-card p{font-size:11.5px;line-height:18.5px;color:var(--text)}

/* about */
.about-band{left:0;top:1363px;width:1200px;height:540px;background:var(--panel)}
.about-copy p{font-size:12.8px;line-height:22.5px;color:var(--text);margin-bottom:14px}

/* testimonials */
.nav-btn{width:34px;height:34px;border-radius:50%;display:flex;align-items:center;justify-content:center}
.quote{position:absolute;top:2147px;width:380px;height:233px;border:1px solid var(--card-line);border-radius:8px;background:var(--white);padding:62px 30px 0 31px}
.quote.raised{border:none;box-shadow:0 6px 22px rgba(0,0,0,.08)}
.quote p{font-size:11.5px;line-height:20px;color:var(--text)}
.quote h4{font-size:15px;font-weight:600;margin-top:20px}
.stars{color:#f3a51c;font-size:16px;letter-spacing:3px}
.avatar{position:absolute;top:2107px;width:68px;height:68px;border-radius:50%;border:4px solid var(--white);box-shadow:0 3px 10px rgba(0,0,0,.12)}

/* what we do */
.do-panel{left:333px;top:2530px;width:725px;height:495px;background:var(--panel);border-radius:14px}
.do-item{position:absolute;left:595px;display:flex;gap:16px}
.do-item .ic{width:46px;height:46px;border-radius:50%;background:var(--green);flex:none;display:flex;align-items:center;justify-content:center}
.do-item h4{font-size:16px;font-weight:600;margin-bottom:6px}
.do-item p{font-size:11.5px;line-height:18.5px;color:var(--text);width:340px}

/* footer */
.footer{left:0;top:3585px;width:1200px;height:544px;background:var(--footer);color:var(--footer-text)}
.footer .cta{left:141px;top:50px;font-size:36px;line-height:52px;color:var(--white)}
.footer .line{left:141px;width:917px;height:1px;background:#4a4a4a}
.footer-brand{left:141px;top:262px;width:230px;display:flex;align-items:flex-start;gap:12px;font-size:26px;line-height:34px;font-weight:600;color:var(--white)}
.footer-brand .dot{width:18px;height:18px;margin-top:8px;border-radius:50%;background:var(--green);flex:none}
.fcol h5{font-size:17px;font-weight:600;color:var(--green);margin-bottom:18px}
.fcol li{list-style:none;font-size:12.5px;color:var(--footer-text);margin-bottom:14px;display:flex;align-items:center;gap:10px;white-space:nowrap}
.soc{width:22px;height:22px;border-radius:50%;background:var(--green);flex:none}
</style>
</head>
<body>

<!-- HERO -->
<div class="abs hero-bg"></div>
<div class="abs hero-arc"></div>
<div class="abs hero-photo" role="img" aria-label="Modern two-storey timber and glass home with a dark car parked in front at dusk"></div>
<div class="abs brand"><span class="dot"></span>Varrow Constructions</div>

<div class="abs top-contact" style="left:560px">
  <svg width="16" height="12" viewBox="0 0 16 12"><rect x="0.5" y="0.5" width="15" height="11" rx="1.5" fill="#222"/><path d="M1 1l7 6 7-6" stroke="#fff" fill="none"/></svg>
  info@varrowconstructions.com
</div>
<div class="abs top-contact" style="left:818px">
  <svg width="14" height="14" viewBox="0 0 24 24"><path fill="#222" d="M6.6 10.8a15 15 0 006.6 6.6l2.2-2.2a1 1 0 011-.25 11.4 11.4 0 003.6.57 1 1 0 011 1V20a1 1 0 01-1 1A17 17 0 013 4a1 1 0 011-1h3.5a1 1 0 011 1c0 1.25.2 2.45.57 3.57a1 1 0 01-.25 1z"/></svg>
  123-456-7890
</div>
<a class="btn" style="left:955px;top:28px;width:146px;height:38px">Contact Us<span class="arrow"><svg width="16" height="12" viewBox="0 0 16 12"><path d="M1 6h13M9 1l5 5-5 5" stroke="#222" stroke-width="1.6" fill="none"/></svg></span></a>

<div class="abs discover-line"></div>
<div class="abs discover">Discover More</div>
<div class="abs mouse"></div>

<h1 class="abs display hero-title">building your<br>dream home in<br>australia.</h1>
<p class="abs hero-sub">We transform your vision into a luxurious haven that<br>whispers elegance with every detail.</p>
<a class="btn" style="left:140px;top:444px;width:205px;height:38px">Explore Our Projects<span class="arrow"><svg width="16" height="12" viewBox="0 0 16 12"><path d="M1 6h13M9 1l5 5-5 5" stroke="#222" stroke-width="1.6" fill="none"/></svg></span></a>

<!-- SERVICES -->
<h2 class="abs display section-title" style="left:0;top:595px">our services<span class="rule"></span></h2>

<div class="svc photo" style="left:141px;top:697px;background:linear-gradient(170deg,#c9d6e0,#8a6d52 55%,#3c3f35)" role="img" aria-label="Contemporary multi-level home with timber cladding and balconies"></div>
<div class="svc svc-card" style="left:459px;top:697px">
  <svg width="58" height="58" viewBox="0 0 58 58" fill="none" stroke="#7dc242" stroke-width="2.4" stroke-linecap="round" stroke-linejoin="round"><path d="M10 48L36 22M36 22l6-2 6-8-4-4-8 6-2 6"/><path d="M14 10a8 8 0 0010 10l24 24-4 4-24-24A8 8 0 0110 14l5 5 4-4z"/></svg>
  <h3>Renovations</h3>
  <p>It is a long established fact that a reader will be distracted by the readable content of a page when looking at its layout. The point of using Lorem Ipsum is that it has a more-or-less normal distribution of letters.</p>
</div>
<div class="svc photo" style="left:776px;top:697px;background:linear-gradient(170deg,#6fa3dd,#c7b49a 55%,#7f6a55)" role="img" aria-label="New house under construction with timber frame and blue sky"></div>

<div class="svc svc-card" style="left:141px;top:1005px">
  <svg width="60" height="58" viewBox="0 0 60 58" fill="none" stroke="#7dc242" stroke-width="2.4" stroke-linejoin="round"><path d="M6 28L30 6l24 22M12 23v30h36V23M4 53h52"/><rect x="22" y="24" width="16" height="14"/><path d="M30 24v14M22 31h16"/></svg>
  <h3>Custom Home Building</h3>
  <p>It is a long established fact that a reader will be distracted by the readable content of a page when looking at its layout. The point of using Lorem Ipsum is that it has a more-or-less normal distribution of letters.</p>
</div>
<div class="svc photo" style="left:459px;top:1005px;background:linear-gradient(160deg,#f1ece3,#cbbba4 60%,#8f7c65)" role="img" aria-label="Bright interior being renovated with ladder and open glass doors"></div>
<div class="svc svc-card" style="left:776px;top:1005px">
  <svg width="62" height="58" viewBox="0 0 62 58" fill="none" stroke="#7dc242" stroke-width="2.4" stroke-linejoin="round"><path d="M4 26L26 6l22 20M10 21v31h32V21"/><rect x="18" y="28" width="16" height="13"/><path d="M26 28v13M18 34h16"/><rect x="42" y="32" width="16" height="20"/><path d="M50 38v8M46 42h8"/></svg>
  <h3>Extensions</h3>
  <p>It is a long established fact that a reader will be distracted by the readable content of a page when looking at its layout. The point of using Lorem Ipsum is that it has a more-or-less normal distribution of letters.</p>
</div>

<!-- ABOUT -->
<div class="abs about-band"></div>
<div class="photo" style="left:141px;top:1420px;width:345px;height:428px;border-radius:12px;background:linear-gradient(170deg,#1f3c55,#3e4a52 45%,#b17a43 70%,#1c2a33)" role="img" aria-label="Modern three-storey home lit up at night beside water"></div>
<h2 class="abs display" style="left:585px;top:1458px;font-size:38px">about varrow<span class="rule"></span></h2>
<div class="abs about-copy" style="left:585px;top:1538px;width:462px">
  <p>There are many variations of passages of Lorem Ipsum available, but the majority have suffered alteration in some form, by injected humour, or randomised words which don't look even slightly believable. If you are going to use a passage of Lorem Ipsum, you need to be sure there isn't anything embarrassing hidden in the middle of text.</p>
  <p>It is a long established fact that a reader will be distracted by the readable content of a page when looking at its layout. The point of using Lorem Ipsum is that it has a more-or-less normal distribution of letters.</p>
</div>
<a class="btn" style="left:585px;top:1763px;width:150px;height:38px">Get Started<span class="arrow"><svg width="16" height="12" viewBox="0 0 16 12"><path d="M1 6h13M9 1l5 5-5 5" stroke="#222" stroke-width="1.6" fill="none"/></svg></span></a>
<div class="abs" style="left:900px;top:1745px;width:255px;height:190px;border-radius:50% 50% 12px 12px;background:linear-gradient(180deg,#d9dde2,#8fa07a 70%,#5f8f3a)" role="img" aria-label="Small 3D illustration of a house on a green lawn"></div>

<!-- TESTIMONIALS -->
<h2 class="abs display" style="left:141px;top:2010px;font-size:38px">what our clients say<span class="rule"></span></h2>
<div class="abs nav-btn" style="left:975px;top:2027px;border:1.5px solid #333">
  <svg width="10" height="12" viewBox="0 0 10 12"><path d="M7 1L2 6l5 5" stroke="#222" stroke-width="1.8" fill="none"/></svg></div>
<div class="abs nav-btn" style="left:1024px;top:2027px;background:#222">
  <svg width="10" height="12" viewBox="0 0 10 12"><path d="M3 1l5 5-5 5" stroke="#fff" stroke-width="1.8" fill="none"/></svg></div>

<div class="quote" style="left:141px">
  <p>All the Lorem Ipsum generators on the Internet tend to repeat predefined chunks as necessary, making this the first true generator on the Internet. It uses a dictionary of over 200 Latin words.</p>
  <h4>Dana Whitlow</h4><div class="stars">★★★★★</div>
</div>
<div class="quote raised" style="left:542px">
  <p>All the Lorem Ipsum generators on the Internet tend to repeat predefined chunks as necessary, making this the first true generator on the Internet. It uses a dictionary of over 200 Latin words.</p>
  <h4>Owen Carrick</h4><div class="stars">★★★★★</div>
</div>
<div class="quote" style="left:943px">
  <p>All the Lorem Ipsum generators on the Internet tend to repeat predefined chunks as necessary, making this the first true generator on the Internet. It uses a dictionary of over 200 Latin words.</p>
  <h4>Lena Paskett</h4><div class="stars">★★★★★</div>
</div>
<div class="avatar" style="left:175px;background:linear-gradient(#e6d3c8,#b44a4a)" role="img" aria-label="Client portrait photo"></div>
<div class="avatar" style="left:576px;background:linear-gradient(#d8d3cc,#5a5a5a)" role="img" aria-label="Client portrait photo"></div>
<div class="avatar" style="left:977px;background:linear-gradient(#e6e9ee,#7a96b8)" role="img" aria-label="Client portrait photo"></div>

<!-- WHAT WE DO -->
<div class="abs do-panel"></div>
<div class="photo" style="left:141px;top:2472px;width:400px;height:465px;border-radius:12px;background:linear-gradient(170deg,#c8d7e4,#ece8e2 40%,#9a7356 70%,#4f5a3c)" role="img" aria-label="White modern townhouse with timber screens and garden"></div>
<h2 class="abs display" style="left:595px;top:2570px;font-size:38px">what we do<span class="rule"></span></h2>
<p class="abs" style="left:595px;top:2650px;width:420px;font-size:13px;line-height:22px;font-weight:500">It is a long established fact that a reader will be distracted by the readable content of a page when looking at its layout.</p>
<div class="do-item" style="top:2718px"><span class="ic"><svg width="22" height="22" viewBox="0 0 22 22" fill="none" stroke="#fff" stroke-width="1.8"><rect x="4" y="3" width="14" height="17"/><path d="M8 7h2M12 7h2M8 11h2M12 11h2M9 20v-4h4v4"/></svg></span><div><h4>Building</h4><p>Lorem Ipsum is simply dummy text of the printing and typesetting industry.</p></div></div>
<div class="do-item" style="top:2814px"><span class="ic"><svg width="22" height="22" viewBox="0 0 22 22" fill="none" stroke="#fff" stroke-width="1.8"><path d="M4 20V4h2v16M4 5h15l-3 4M6 9h10"/></svg></span><div><h4>Construction</h4><p>There are many variations of passages of Lorem Ipsum available, but the majority have suffered alteration.</p></div></div>
<div class="do-item" style="top:2910px"><span class="ic"><svg width="22" height="22" viewBox="0 0 22 22" fill="none" stroke="#fff" stroke-width="1.8"><rect x="3" y="4" width="16" height="14"/><path d="M6 15l4-6 3 4 2-2 2 4"/></svg></span><div><h4>Design</h4><p>It is a long established fact that a reader will be distracted by the readable content of a page when looking at its layout.</p></div></div>

<!-- GALLERY -->
<h2 class="abs display section-title" style="left:0;top:3098px">project gallery<span class="rule"></span></h2>
<div class="photo" style="left:-10px;top:3230px;width:222px;height:195px;background:linear-gradient(160deg,#efeae3,#c9b79e)" role="img" aria-label="Living room with staircase"></div>
<div class="photo" style="left:234px;top:3200px;width:230px;height:115px;background:linear-gradient(160deg,#8a6a4e,#c56a2e)" role="img" aria-label="Lounge with orange sofas"></div>
<div class="photo" style="left:234px;top:3335px;width:230px;height:143px;background:linear-gradient(170deg,#b9cadb,#e8e6e2 50%,#6a7a4b)" role="img" aria-label="Modern home exterior with lawn"></div>
<div class="photo" style="left:485px;top:3200px;width:230px;height:300px;background:linear-gradient(170deg,#c5b9ad,#6e5646 60%,#3a3632)" role="img" aria-label="Gabled family home at dusk"></div>
<div class="photo" style="left:735px;top:3200px;width:230px;height:148px;background:linear-gradient(170deg,#93b3d6,#8a7560 60%,#4d6b37)" role="img" aria-label="Contemporary house on a hill"></div>
<div class="photo" style="left:735px;top:3368px;width:230px;height:110px;background:linear-gradient(160deg,#f1ebe0,#e0b040)" role="img" aria-label="Sunny living room with yellow sofa"></div>
<div class="photo" style="left:985px;top:3250px;width:225px;height:178px;background:linear-gradient(160deg,#eee8de,#b8a58d)" role="img" aria-label="Neutral living room interior"></div>

<!-- FOOTER -->
<footer class="abs footer">
  <h2 class="abs display cta">get a free consultancy<br>right now</h2>
  <a class="btn" style="left:912px;top:91px;width:146px;height:38px">Contact Us<span class="arrow"><svg width="16" height="12" viewBox="0 0 16 12"><path d="M1 6h13M9 1l5 5-5 5" stroke="#222" stroke-width="1.6" fill="none"/></svg></span></a>
  <div class="abs line" style="top:190px"></div>

  <div class="abs footer-brand"><span class="dot"></span><span>Varrow<br>Constructions</span></div>

  <div class="abs fcol" style="left:420px;top:250px"><h5>Resources</h5><ul><li>Privacy Policy</li><li>Terms Of Service</li><li>Contact Us</li></ul></div>
  <div class="abs fcol" style="left:637px;top:250px"><h5>Follow Us</h5><ul><li><span class="soc"></span>Photo Feed</li><li><span class="soc"></span>Short Posts</li><li><span class="soc"></span>Community</li><li><span class="soc"></span>Pro Network</li></ul></div>
  <div class="abs fcol" style="left:850px;top:250px"><h5>Contact Info</h5><ul>
    <li><svg width="14" height="18" viewBox="0 0 14 18"><path d="M7 1a6 6 0 00-6 6c0 4.5 6 10 6 10s6-5.5 6-10a6 6 0 00-6-6z" fill="none" stroke="#fff" stroke-width="1.5"/><circle cx="7" cy="7" r="2" fill="#fff"/></svg><span>123 Lorem ipsum dummy,<br>#567 Dummy road 1234</span></li>
    <li><svg width="16" height="12" viewBox="0 0 16 12"><rect x="0.5" y="0.5" width="15" height="11" rx="1.5" fill="#fff"/><path d="M1 1l7 6 7-6" stroke="#262626" fill="none"/></svg>info@varrowconstructions.com</li>
    <li><svg width="14" height="14" viewBox="0 0 24 24"><path fill="#fff" d="M6.6 10.8a15 15 0 006.6 6.6l2.2-2.2a1 1 0 011-.25 11.4 11.4 0 003.6.57 1 1 0 011 1V20a1 1 0 01-1 1A17 17 0 013 4a1 1 0 011-1h3.5a1 1 0 011 1c0 1.25.2 2.45.57 3.57a1 1 0 01-.25 1z"/></svg>123-456-7890</li>
  </ul></div>

  <div class="abs line" style="top:455px"></div>
  <p class="abs" style="left:0;top:500px;width:1200px;text-align:center;font-size:12.5px">© 2024 Varrow Constructions. All Rights Reserved.</p>
</footer>

</body>
</html>
```